Plakat-Design für Blasmusik Konzert
Zielgruppe
Wir - die Tordinger Blasmusik e.V. - sind auf der Suche nach:
einem Plakatdesign in A1 & A2 und passendem
Ticket-Design DIN lang quer inkl. Perforierung und 2x Nummerierung
für unser Konzert 2019 mit dem Motto:
'NIGHTS OF WONDER'.
Das Konzert wird einen weiten Rahmen von Henrik Dallmann und Brisko hin zu Bernd Falkenrath und Tom Kellin. Auch Titel aus dem Bereich Filmmusik wird es geben. Also ein bunter Abend mit Gesang und Showlicht.
Wir freuen uns auf eure Ideen!!!
Impressionen: www.tordinger-blasmusik.de
Aufgabenstellung
Stichworte: Bunt, Modern, Edel
Facts:
Samstag 05.10.2019 Beginn 19:00
Festsaal im Lindenhof, Kellbach am See
Eintritt 15€, Kinder bis einschließlich 8 Jahre Eintritt frei.
'Mehr Informationen unter www.tordinger-blasmusik.de und auf Plaudernet'
Für Ticket: Einlass ab 18:30 Uhr. Freie Platzwahl.
Irgendwo auf dem Plakat muss Platz für die dezente Nennung von 2-3 Sponsoren vorgesehen werden. Diese würden wir nachträglich einfügen. Auch ein 'Find us on Plaudernet'-Icon wäre cool.
Die Druckdateien (CMYK) sind mit entsprechendem Beschnitt gemäß Vorgabe von 'flott-gedruckt-jetzt' anzulegen und als Vector-Datei sowie PDF zu übergeben.

```html
<!DOCTYPE html>
<html lang="de">
<head>
<meta charset="utf-8">
<title>Nights of Wonder – Konzert 2019</title>
<link rel="stylesheet" href="https://fonts.googleapis.com/css2?family=Bebas+Neue&family=Fira+Sans:ital,wght@0,500;0,600;1,500&display=swap">
<style>
  :root {
    --backdrop: #2b2b2b;
    --poster-bg: #585858;
    --white: #ffffff;
    --purple: #6a2870;
    --splash-pink: #e84aa8;
    --splash-cyan: #5fd3e6;
    --splash-blue: #3b5bd6;
    --splash-yellow: #f3d34a;
    --splash-violet: #8a3bb8;
  }
  * { margin: 0; padding: 0; box-sizing: border-box; }
  html, body {
    width: 1200px; height: 1200px; overflow: hidden;
    background: var(--backdrop);
  }
  .poster {
    position: absolute; left: 198px; top: 30px;
    width: 804px; height: 1140px;
    background: var(--poster-bg);
    overflow: hidden;
    font-family: "Fira Sans", sans-serif;
    color: var(--white);
  }
  .club-name {
    position: absolute; left: 28px; top: 60px;
    font-size: 46px; font-weight: 600; line-height: 1.05;
  }
  .event-facts {
    position: absolute; right: 24px; top: 36px; width: 320px;
    text-align: right;
  }
  .event-date { font-size: 42px; font-weight: 500; line-height: 1.15; }
  .event-time { font-size: 40px; font-weight: 500; line-height: 1.15; }
  .event-rule { height: 2px; background: var(--white); margin: 12px 0 10px 18px; opacity: .85; }
  .event-venue { font-size: 24px; font-style: italic; font-weight: 500; line-height: 1.3; }
  .splash-art {
    position: absolute; left: 22px; top: 183px; width: 763px; height: 790px;
    border-radius: 48% 52% 45% 55% / 50% 45% 55% 50%;
    background:
      radial-gradient(circle at 30% 35%, var(--splash-cyan) 0, transparent 38%),
      radial-gradient(circle at 70% 30%, var(--splash-yellow) 0, transparent 30%),
      radial-gradient(circle at 55% 65%, var(--splash-pink) 0, transparent 45%),
      radial-gradient(circle at 35% 75%, var(--splash-blue) 0, transparent 40%),
      radial-gradient(circle at 50% 50%, var(--splash-violet) 0, rgba(88,88,88,0) 70%);
    opacity: .9;
    filter: blur(6px);
  }
  .headline {
    position: absolute; left: 0; top: 0; width: 804px; height: 1140px;
  }
  .headline text { font-family: "Bebas Neue", sans-serif; fill: var(--white); }
  .price-badge {
    position: absolute; left: 620px; top: 855px; width: 140px; height: 140px;
    border-radius: 50%; background: var(--purple);
    display: flex; flex-direction: column; align-items: center; justify-content: center;
    font-size: 32px; font-weight: 500; line-height: 1.2;
  }
  .footnote {
    position: absolute; right: 20px; top: 1010px;
    font-size: 16px; font-style: italic; font-weight: 500;
  }
  .info-bar {
    position: absolute; left: 0; top: 1044px; width: 804px; height: 96px;
    background: var(--purple);
  }
  .info-label { position: absolute; left: 12px; top: 8px; font-size: 13px; font-weight: 600; }
  .info-line { position: absolute; left: 12px; font-size: 17px; font-weight: 600; display: flex; align-items: center; gap: 6px; white-space: nowrap; }
  .info-social { top: 38px; }
  .info-web { top: 62px; }
  .social-square { width: 13px; height: 13px; background: var(--white); display: inline-block; }
  .sponsor-slot {
    position: absolute; top: 7px; width: 128px; height: 79px; background: var(--white);
  }
</style>
</head>
<body>
  <main class="poster">
    <div class="splash-art" role="img" aria-label="Bunte Farbexplosion mit Blechblasinstrumenten"></div>

    <div class="club-name">Tordinger<br>Blasmusik e.V.</div>

    <div class="event-facts">
      <div class="event-date">Sa. 05.10.2019</div>
      <div class="event-time">Beginn: 19.00</div>
      <div class="event-rule"></div>
      <div class="event-venue">Festsaal im Lindenhof,<br>Kellbach am See</div>
    </div>

    <svg class="headline" viewBox="0 0 804 1140" aria-label="Nights of Wonder – Konzert 2019">
      <defs>
        <filter id="title-shadow" x="-10%" y="-10%" width="120%" height="130%">
          <feDropShadow dx="0" dy="4" stdDeviation="5" flood-color="#000" flood-opacity=".45"/>
        </filter>
      </defs>
      <g filter="url(#title-shadow)">
        <text x="116" y="498" font-size="262" textLength="570" lengthAdjust="spacingAndGlyphs">NIGHTS</text>
        <text x="60" y="705" font-size="262" textLength="684" lengthAdjust="spacingAndGlyphs">OF WONDER</text>
        <text x="395" y="813" font-size="86" text-anchor="middle">KONZERT 2019</text>
      </g>
    </svg>

    <div class="price-badge"><span>Eintritt</span><span>15€*</span></div>

    <div class="footnote">*Kinder bis einschließlich 8 Jahre Eintritt frei.</div>

    <footer class="info-bar">
      <div class="info-label">Mehr Informationen :</div>
      <div class="info-line info-social"><span class="social-square"></span>plaudernet.com/Tordinger-Blasmusik-eV</div>
      <div class="info-line info-web">www.tordinger-blasmusik.de</div>
      <div class="sponsor-slot" style="left:392px"></div>
      <div class="sponsor-slot" style="left:531px"></div>
      <div class="sponsor-slot" style="left:669px"></div>
    </footer>
  </main>
</body>
</html>
```